Homepage für Gartenfirma
Zielgruppe
Garten- und Landschaftsbau, Gartenpflege, Gartenbau, Gärtnerei, Gartengestaltung
Hallo liebe Designer,
nachdem ich auch über diese Plattform mein Logo erstellen lassen haben (s. Anhang), möchten ich nun einen Schritt weiter gehen und auch meine Internet-Seite hierüber designen lassen.
Den Auftrag zur Programmierung werde ich seperat im Nachgang starten.
Jedoch bin ich für eure Info dankbar, ob Ihr jeweiliges Design selbst umsetzen könnt.
Nun zu meinen Vorstellungen bezüglich des Designs.
An dem ausgewählten Logo könnt Ihr bereits erste Eindrücke über meinen Geschmack und meine Vorstellungen zum Design gewinnen.
Ich würde es als modern, dezent, innovativ und seriös beschreiben.
Die Homepage sollte genau so aussehen und wirken.
Vielleicht hilft euch die Beschreibung, dass ich mir eine dezente Art und Weise wie bei Quince vorstelle :)
Ich wünsche mir einen komplett weissen Hintergrund.
Bitte auch keine Rahmen hinterlegen, in denen der Fliestext hinterlegt ist.
Die Seite sollte in keinem Fall mit der Farbe grün übersättigt werden. Im Gegenteil: Es sollte dezent eingearbeitet werden.
Ich denke die Schrift sollte sicherlich in grün gehalten werden.
Sollte es an der ein oder anderen Stelle ein Grün geben (banner oder was auch immer),dann könnte man hier eine weisse Schriftfarbe verwenden.
Im Internet habe ich nicht wirklich viele inspirierende Internetseiten von vergleichbaren Firmen gefunden, obwohl es so viele Wettbewerber auf dem Markt gibt.
Als ungefähre Orientierung kann ich euch lediglich folgende Seiten benennen:
http://gartenbau-lindmoor.example/home/
http://www.wertak-galabau.example/ (finde ich bisher am besten)
Ich stelle mir ebenfalls hochauflösende Bilder auf der Homepage vor, die in direktem Zusammenhang mit der Branche stehen und auch durchs Bild „gleiten“. Jedoch nicht langgezogen von einem Bildrand zum anderen.
Die Bilder sollten bitte seeehr gut ausgewählt und sehr ästethisch sein!!
Die Schriftart sollte ..

```html
<!DOCTYPE html>
<html lang="de">
<head>
<meta charset="utf-8">
<title>Blatthain – Garten- und Landschaftsbau</title>
<link rel="stylesheet" href="https://fonts.googleapis.com/css2?family=Lato:wght@400;700;900&display=swap">
<style>
  :root {
    --green: #7dc21e;
    --text: #3a3a3a;
    --nav: #4a4a4a;
    --white: #ffffff;
    --page: #fafafa;
    --band: #f1f1f1;
    --footer: #3d3d3d;
  }
  * { margin: 0; padding: 0; box-sizing: border-box; }
  html, body { width: 876px; height: 1200px; overflow: hidden; }
  body {
    position: relative;
    background: var(--page);
    font-family: "Lato", sans-serif;
    color: var(--text);
  }
  .site-header { position: absolute; left: 0; top: 0; width: 876px; height: 87px; background: var(--page); }
  .brand { position: absolute; left: 72px; top: 30px; display: flex; align-items: center; gap: 12px; }
  .brand-square { width: 28px; height: 28px; background: var(--green); }
  .brand-name { font-size: 26px; font-weight: 700; color: var(--green); letter-spacing: 0.5px; }
  .main-nav { position: absolute; top: 51px; left: 0; width: 876px; }
  .main-nav a {
    position: absolute; font-size: 11.5px; font-weight: 400; color: var(--nav);
    text-decoration: none; letter-spacing: 0.2px; white-space: nowrap;
  }
  .nav-active-bar { position: absolute; left: 502px; top: 0; width: 62px; height: 5px; background: var(--green); }

  .hero {
    position: absolute; left: 0; top: 87px; width: 876px; height: 398px;
    background:
      radial-gradient(ellipse at 75% 55%, rgba(214,40,140,0.55), transparent 45%),
      radial-gradient(ellipse at 10% 60%, rgba(255,255,255,0.6), transparent 35%),
      linear-gradient(180deg, #d9e64a 0%, #b8c94a 35%, #8a7a3a 75%, #a0642e 100%);
  }
  .hero-title {
    position: absolute; left: 0; top: 207px; width: 876px; text-align: center;
    font-size: 54px; font-weight: 900; color: var(--white); letter-spacing: -0.5px;
  }
  .hero-button {
    position: absolute; left: 305px; top: 300px; width: 273px; height: 54px;
    background: var(--white); border: 7px solid var(--green);
    display: flex; align-items: center; justify-content: center;
    font-size: 14px; font-weight: 700; color: #555; text-decoration: none;
  }

  .feature { position: absolute; left: 0; width: 876px; }
  .feature-1 { top: 485px; height: 236px; background: var(--page); }
  .feature-2 { top: 721px; height: 225px; background: var(--band); }
  .feature-3 { top: 946px; height: 224px; background: var(--page); }
  .feature-text { position: absolute; width: 310px; }
  .feature-title { font-size: 17px; font-weight: 400; color: var(--green); margin-bottom: 12px; }
  .feature-copy { font-size: 11.3px; line-height: 16.4px; color: var(--text); letter-spacing: -0.1px; }
  .learn-more {
    display: flex; align-items: center; justify-content: center;
    width: 96px; height: 26px; margin-top: 19px;
    border: 2px solid var(--green); color: var(--green);
    font-size: 8.5px; font-weight: 700; text-decoration: none;
  }
  .feature-photo { position: absolute; width: 309px; height: 160px; }
  .photo-bike { background: linear-gradient(160deg, #7dbb3c 0%, #5d2f8a 40%, #a5422e 60%, #6cae2f 100%); }
  .photo-plan { background: linear-gradient(135deg, #c9d9a0 0%, #7ea65a 35%, #e8d6a8 65%, #d9c48a 100%); }
  .photo-planting { background: linear-gradient(150deg, #5a6b2a 0%, #9a7ab0 45%, #b9c94a 65%, #c4b8a8 100%); }

  .site-footer {
    position: absolute; left: 0; top: 1170px; width: 876px; height: 30px;
    background: var(--footer); color: var(--white);
    font-size: 6px; font-weight: 700; display: flex; align-items: center; justify-content: center;
  }
</style>
</head>
<body>
  <header class="site-header">
    <div class="brand">
      <div class="brand-square"></div>
      <span class="brand-name">BLATTHAIN</span>
    </div>
    <nav class="main-nav">
      <span class="nav-active-bar" style="top:-51px"></span>
      <a href="#" style="left:505px">ÜBER UNS</a>
      <a href="#" style="left:577px">DIENSTLEISTUNGEN</a>
      <a href="#" style="left:700px">GALERIE</a>
      <a href="#" style="left:763px">KONTAKTE</a>
    </nav>
  </header>

  <section class="hero" role="img" aria-label="Gärtnerin mit Kräutertopf zwischen blühenden Margeriten und Petunien, Gartenwerkzeug auf Holztisch">
    <h1 class="hero-title">WIR SIND KREATIV</h1>
    <a class="hero-button" href="#">GEHEN SIE ZUR GALERIE</a>
  </section>

  <section class="feature feature-1">
    <div class="feature-text" style="left:125px;top:54px">
      <h2 class="feature-title">Leistung</h2>
      <p class="feature-copy">Lorem ipsum dolor sit amet, consectetur adipiscing elit. In ultrices at metus vel ultricies. Integer et aliquet mauris, at congue dolor. Nam efficitur nulla ac justo suscipit suscipit a vel felis.</p>
      <a class="learn-more" href="#">LEARN MORE</a>
    </div>
    <div class="feature-photo photo-bike" style="left:448px;top:45px" role="img" aria-label="Dekoratives rotes Fahrrad mit Blumenkörben auf einer Wiese"></div>
  </section>

  <section class="feature feature-2">
    <div class="feature-photo photo-plan" style="left:125px;top:33px" role="img" aria-label="Hand zeichnet einen farbigen Gartenplan mit Lineal"></div>
    <div class="feature-text" style="left:448px;top:45px">
      <h2 class="feature-title">Gartengestaltung</h2>
      <p class="feature-copy">Lorem ipsum dolor sit amet, consectetur adipiscing elit. In ultrices at metus vel ultricies. Integer et aliquet mauris, at congue dolor. Nam efficitur nulla ac justo suscipit suscipit a vel felis.</p>
      <a class="learn-more" href="#">LEARN MORE</a>
    </div>
  </section>

  <section class="feature feature-3">
    <div class="feature-text" style="left:125px;top:44px">
      <h2 class="feature-title">Bepflanzung</h2>
      <p class="feature-copy">Proin efficitur ante at ex varius, nec ultrices libero gravida. Vivamus at rhoncus massa. Mauris condimentum commodo metus vel sodales. Cras nec leo erat. Quisque tincidunt lacinia feugiat.</p>
      <a class="learn-more" href="#">LEARN MORE</a>
    </div>
    <div class="feature-photo photo-planting" style="left:448px;top:32px" role="img" aria-label="Hände mit Gartenhandschuhen pflanzen Heidekraut in einen Blumenkasten"></div>
  </section>

  <footer class="site-footer">Copyright © 2014. All rights reserved.</footer>
</body>
</html>
```